Web Design Project

We need a web design for a new business in Orland Park, IL.
We are a restaurant meal delivery business. We deliver from a variety of restaurants. We gives our customers an alternative to just pizza delivery.

Websites we like:
http://www.brambleporter.example/
https://www.quillfetchgo.example/Default.asp
www.wendlerunner.example/

Our current website is www.tovenbasket.example(not to be used as a guide, i'm looking for an original design)
Updates

Please no pictures of anything associated with Pizza.  We are a restaurant delivery business that gives our customers an alternative to just pizza delivery. 

This is my original logo.  I uploaded the file to the job brief and updated the brief some.

Target Market(s)

Two income households with children.

Industry/Entity Type

Business

Requirements
Must have
• Order Now button,and sliding photographs of food.
Nice to have
• a background other than white(it can be white if it works with the design)
Should not have
• A picture of pizza that cant be changed. It is ok if the photo is apart of sliding photo's, but pizza cant be the main focus of our delivery service.

```html
<!DOCTYPE html>
<html lang="en">
<head>
<meta charset="utf-8">
<title>Toven Basket – Restaurant Delivery</title>
<link href="https://fonts.googleapis.com/css2?family=Noto+Serif&family=PT+Sans:ital,wght@0,400;0,700;1,700&family=Montserrat:wght@600&display=swap" rel="stylesheet">
<style>
:root{
  --red:#cc0000;
  --red-deep:#b31416;
  --brand-red:#a5161c;
  --yellow:#f8dc74;
  --yellow-hero:#f6df7f;
  --panel:#f4d253;
  --green:#2e6a10;
  --nav-text:#3a2a10;
  --white:#ffffff;
  --card-band:rgba(214,78,78,.78);
}
*{margin:0;padding:0;box-sizing:border-box}
html,body{width:1076px;height:1200px;overflow:hidden}
body{position:relative;background:var(--white);font-family:"PT Sans",Arial,sans-serif}
.abs{position:absolute}

.topbar{left:0;top:0;width:1076px;height:42px;background:var(--red)}
.call{left:74px;top:13px;color:var(--white);font:700 17px "PT Sans",sans-serif}
.phone{left:151px;top:4px;color:var(--white);font:700 28px "PT Sans",sans-serif;letter-spacing:.5px}
.login{left:959px;top:9px;width:64px;height:28px;background:#eee;border:1px solid #999;border-radius:3px;font:400 15px "PT Sans",sans-serif;color:#111;text-align:center;line-height:26px}

.header{left:0;top:42px;width:1076px;height:150px;background:var(--yellow);border-bottom:1px solid #e0c35c}
.brand{left:32px;top:100px;display:flex;align-items:center;gap:8px;color:var(--brand-red);font:700 22px "PT Sans",sans-serif}
.brand-dot{width:16px;height:16px;border-radius:50%;background:var(--brand-red)}
.nav{left:217px;top:90px;display:flex;gap:0;align-items:center}
.nav a{font:400 16px "PT Sans",sans-serif;color:var(--nav-text);text-decoration:none;padding:3px 9px;margin-right:8px}
.nav a.active{background:var(--red);color:var(--white);font-weight:700;border-radius:2px}

.hero{left:0;top:192px;width:1076px;height:364px;background:var(--yellow-hero)}
.hero-title{left:56px;top:213px;font:400 57px "Noto Serif",serif;color:var(--brand-red)}
.order-panel{left:54px;top:298px;width:465px;height:188px;background:var(--panel);border:1px solid #e9c24a;border-radius:3px;box-shadow:0 10px 8px -6px rgba(120,90,20,.35)}
.order-text{left:80px;top:320px;width:420px;font:400 17px/1.15 "PT Sans",sans-serif;color:#3b3320}
.zip{left:80px;top:372px;width:299px;height:30px;background:#e8e2cf;border-radius:3px;color:#b3ad9a;font:400 14px "PT Sans",sans-serif;padding:6px 7px}
.zip svg{position:absolute;right:5px;top:4px}
.start{left:80px;top:424px;width:173px;height:39px;background:var(--green);border-radius:2px;color:var(--white);font:italic 700 17px "PT Sans",sans-serif;padding:9px 14px}
.start svg{position:absolute;right:18px;top:14px}
.hero-photo{left:645px;top:194px;width:323px;height:362px;background:radial-gradient(ellipse at 60% 45%,#fbf7ef 0%,#e9e1cf 40%,rgba(246,223,127,0) 70%)}

.card{top:579px;width:322px;height:208px;border:1px solid #888;overflow:hidden}
.card .band{position:absolute;left:0;top:153px;width:100%;height:41px;background:var(--card-band);color:var(--white);font:600 18px "Montserrat",sans-serif;padding:9px 19px}
.card .band svg{position:absolute;right:14px;top:14px}
.card-restaurants{left:34px;background:linear-gradient(135deg,#c9bfb2,#a89c8d 60%,#d6ccc0)}
.card-corporate{left:377px;background:linear-gradient(180deg,#f4f2f0,#d9d0c8 50%,#4a4e5c)}
.card-order{left:717px;background:linear-gradient(120deg,#c7b59f,#8a5a44 45%,#e9e3dc)}

.footer{left:0;top:818px;width:1076px;height:382px;background:linear-gradient(180deg,var(--red),var(--red-deep))}
.foot-h{top:840px;color:var(--white);font:600 19px "Montserrat",sans-serif}
.about-text{left:45px;top:877px;width:316px;color:var(--white);font:400 13.5px/1.26 Arial,sans-serif;letter-spacing:.3px}
.about-text p+p{margin-top:17px}
.field{left:443px;width:253px;background:var(--white);border-radius:3px;color:#888;font:400 16px Arial,sans-serif;padding:5px 10px;box-shadow:0 4px 4px rgba(0,0,0,.25)}
.send{left:523px;top:1070px;width:90px;height:32px;background:#eee;border:1px solid #999;border-radius:3px;font:400 17px Arial,sans-serif;text-align:center;line-height:30px;color:#111}
.social-dot{left:785px;width:35px;height:35px;border-radius:50%;background:radial-gradient(circle at 40% 35%,#f2f2f2,#b9b9b9)}
.social-label{left:845px;color:var(--white);font:600 16px "Montserrat",sans-serif}
.divider{left:0;top:1129px;width:1076px;height:1px;background:rgba(255,255,255,.3)}
.foot-nav{left:44px;top:1142px;display:flex;gap:19px}
.foot-nav a{color:var(--white);font:400 14px Arial,sans-serif;text-decoration:none}
.copyright{right:39px;top:1174px;color:var(--white);font:400 11px Arial,sans-serif}
</style>
</head>
<body>
<div class="abs topbar"></div>
<div class="abs call">Call us</div>
<div class="abs phone">555 014 2297</div>
<div class="abs login">LOGIN</div>

<header class="abs header"></header>
<div class="abs brand"><span class="brand-dot"></span>Toven Basket</div>
<nav class="abs nav">
  <a class="active" href="#">Home</a><a href="#">Restaurants</a><a href="#">How Do I Order?</a><a href="#">Corporate</a><a href="#">Gift Certificate</a><a href="#">About Us</a><a href="#">Contact Us</a><a href="#">Comments</a>
</nav>

<section class="abs hero"></section>
<h1 class="abs hero-title">Ready to order!</h1>
<div class="abs order-panel"></div>
<p class="abs order-text">Select your zip code and find the restaurants closet to you and order now.</p>
<div class="abs zip">Select your zip code
  <svg width="14" height="22" viewBox="0 0 14 22"><path d="M7 1 13 9H1Z M7 21 1 13h12Z" fill="#a9a496"/></svg>
</div>
<div class="abs start">Start your order
  <svg width="9" height="12" viewBox="0 0 9 12"><path d="M0 0 9 6 0 12Z" fill="#fff"/></svg>
</div>
<div class="abs hero-photo" role="img" aria-label="Smiling chef in white uniform holding an open takeout box of food"></div>

<div class="abs card card-restaurants" role="img" aria-label="Restaurant stone wall sign">
  <div class="band">Restaurants<svg width="20" height="14" viewBox="0 0 20 14"><path d="M1 1 7 7 1 13M10 1l6 6-6 6" stroke="#fff" stroke-width="3" fill="none"/></svg></div>
</div>
<div class="abs card card-corporate" role="img" aria-label="Group of office colleagues">
  <div class="band">Corporate<svg width="20" height="14" viewBox="0 0 20 14"><path d="M1 1 7 7 1 13M10 1l6 6-6 6" stroke="#fff" stroke-width="3" fill="none"/></svg></div>
</div>
<div class="abs card card-order" role="img" aria-label="Woman ordering on a laptop">
  <div class="band">How do I order<svg width="20" height="14" viewBox="0 0 20 14"><path d="M1 1 7 7 1 13M10 1l6 6-6 6" stroke="#fff" stroke-width="3" fill="none"/></svg></div>
</div>

<footer class="abs footer"></footer>
<h2 class="abs foot-h" style="left:45px">About Toven Basket</h2>
<div class="abs about-text">
  <p>Lorem ipsum dolor sit amet, sea cu ceteros pertinacia, blandit voluptaria eam te. At possit percipit vel. Sonet sanctus appetere no sea. Usu ei quaeque omittantur, te porro tacimates qui, cum civibus petentium mnesarchum et. Zril phaedrum petentium est te, nostrum expetendis eu ius, debet facete consectetuer pri ex.</p>
  <p>Mea te gloriatur theophrastus. At liber dolorum vim. Ut viderer graecis cum, feugiat epicuri aliquando id eos, prima corpora instructior et vix. Vix congue tibique ei, tacimates postulant intellegat pri et, mei an paulo ullamcorper.</p>
</div>
<h2 class="abs foot-h" style="left:443px">Contact us</h2>
<div class="abs field" style="top:883px;height:29px">Name</div>
<div class="abs field" style="top:924px;height:29px">Email</div>
<div class="abs field" style="top:964px;height:92px">Info</div>
<div class="abs send">Send</div>
<h2 class="abs foot-h" style="left:784px">Social Contact</h2>
<div class="abs social-dot" style="top:880px"></div>
<div class="abs social-label" style="top:885px">Friendwall</div>
<div class="abs social-dot" style="top:936px"></div>
<div class="abs social-label" style="top:943px">Chirpline</div>
<div class="abs divider"></div>
<nav class="abs foot-nav">
  <a href="#">Home</a><a href="#">Restaurants</a><a href="#">How Do I Order?</a><a href="#">Corporate</a><a href="#">Gift Certificate</a><a href="#">About Us</a><a href="#">Contact Us</a><a href="#">Comments</a>
</nav>
<div class="abs copyright">Copyright 2013 Toven Basket. All rights reserved.</div>
</body>
</html>
```